Wordpress Design Project

WHO WE ARE:
Bright Path Web Growth is not just another SEO or PPC company. We work with our clients to help them grow their business and achieve their goals. Our commitment to doing what is best for the customer, is why we have grown so quickly. We believe our business is not about advertising BUT about connecting customers & growing our clients businesses. We see our product as helping people, not selling a product.

PROJECT OVERVIEW:
I need to create a wordpress website for my business, www.brightpathwebgrowth.com.au

I need a whole new site created showing all of my services. The services include:
NOTE: These are not the main focus of the home page.

Consulting & Strategy Planning
Search Engine Optimisation
Pay Per Click
Re-Marketing

Once I have selected the top home page design, I will need a product and blog page designed.

SITE DESIGN:
If I was to explain the kind of style I am looking for, it would be high-street, New York agency look, web 2.0. Clean, elegant, stylish, high quality and simple looking. Kind of like you would expect from an quince website.

Think of car advertising, the closest to the target market & look/feel Im looking for would be Ravenmotor, Korel, Tamar, Brandin, Zepra.

However, I am open to any design style.

DO NOT let this restrict your creativity BUT here are some websites I like the look of.

Home page:
http://www.layoutfoundry.example/demo/52816.html
https://www.vantorix.example/intl/en/halo/devices/
http://www.vantorix.example/intl/en/halo/devices/features-different.html
http://www.layoutfoundry.example/demo/47190.html
https://www.vantorix.example/intl/en/halo/browser/features.html

Product Page:
http://www.vantorix.example/intl/en/halo/devices/buynow.html#instore

NOTE: I just added a file called "I like this color scheme.png" you can play around with something like this as well.
Updates

Please do not use the content from my current website. That is for a PPC service, the new site is for an full service agency.

Also, the message/tagline is the feature or most prominent element of the website..... Not the services we offer, these are secondary.

Great designs so far everyone, but I think I'm looking a little simpler and less crowded.  Closer to the sample sites I sent.... keep em coming.

Also, I would prefer that the 4 services, do not visually over power the tag line.  The 4 services are not important to the home page.

Lets make this easy, since every design I receive is almost the same...

Make the design look something like these 2 websites.
https://www.vantorix.example/intl/en/halo/browser/features.html#simplicity

Target Market(s)

Business Owners and entreprenuers who are well established, typically in the 35-60 year old range and spend 100k-1m in advertising per year. They big brands that target these people are Ravenmotor, Korel, Tamar, Brandin, Zepra, this should give you the feel for what I am after.

Industry/Entity Type

Advertising

Requirements
Must have
• 1. Navigations: Home, Services, About Us, Blog, Contact Us

2. The main home page words should be.... "We Grow Your Business Online" and "Clear Aim, Clear Plan, Clear Team, Bright Path Web Growth" (should use logo for last one)
I would like to see this tagline somewhere in the site "We Don't Want to be the Biggest, Just the Best!"

3. Product page must have a contact form with (name, email, phone, website)
This form must show an offer of "Free Strategy Sessions, Double your website leads", I have included an image to show as an example for the lead form "lead form example.png", see attached.

Nice to have
• I would like to see 1 or 2 of these idea's in the design.

1. I have attached some logos for Bidlane & Metricove certifications + Web association logo you can use for design purposes.

2. You can put company logo's in the design and I can change them to my clients logos at a later date.

3. Testimonials

4. Since our business is about people, pictures of people like business owners, customers using technology such as an slate, or anything like that would be good. However, is not necessary. Some idea: http://www.peerlattice.example/advertising
Should not have
• There will be no video on the design.

```html
<!DOCTYPE html>
<html lang="en">
<head>
<meta charset="utf-8">
<title>Bright Path Web Growth</title>
<link rel="stylesheet" href="https://fonts.googleapis.com/css2?family=Source+Sans+3:wght@400;600;700&family=Kaushan+Script&display=swap">
<style>
:root{
  --ink:#555;
  --ink-dark:#4a4a4a;
  --text:#666;
  --brand:#1c5aa8;
  --nav-bg:#e5e5e5;
  --rule:#d4d4d4;
  --band:#8c8c8c;
  --strip:#ececec;
  --quote-mark:#3f5f92;
  --client:#9aa6b8;
  --white:#fff;
}
*{box-sizing:border-box;margin:0;padding:0}
html,body{width:1200px;height:1046px;overflow:hidden;background:var(--white)}
body{position:relative;font-family:"Source Sans 3",Arial,sans-serif;color:var(--text)}
.abs{position:absolute}
.account{top:8px;left:834px;font-size:7.5px;color:#444;word-spacing:6px}
.logo{display:flex;align-items:center;gap:8px;color:var(--brand);font-size:15px;line-height:15px;font-weight:600;white-space:nowrap}
.logo .dot{width:34px;height:34px;border-radius:50%;background:var(--brand);flex:none}
.site-logo{top:41px;left:319px}
.nav{top:42px;left:486px;width:396px;height:33px;background:var(--nav-bg);display:flex;justify-content:space-around;align-items:center;font-size:11px;color:#555}
.rule{left:0;width:1200px;height:2px;background:var(--rule)}
.hero-title{top:176px;left:317px;font-size:38px;line-height:43px;color:var(--ink);font-weight:400;white-space:nowrap}
.hero-title b{font-weight:700;color:var(--ink-dark)}
.tagline{top:302px;left:316px;width:276px;text-align:center;font-family:"Kaushan Script",cursive;color:var(--brand);font-size:16px;line-height:28px}
.hero-photo{top:105px;left:640px;width:242px;height:322px;background:linear-gradient(180deg,#cfcfcf 0%,#6e6e6e 45%,#2b2b2b 100%)}
.service{width:272px}
.service .head{display:flex;align-items:center;gap:12px;height:40px;font-size:16px;line-height:18px;color:#555}
.service p{margin-top:14px;font-size:7.7px;line-height:10.7px;color:#666}
.service .more{margin-top:11px;font-size:7.7px;font-weight:700;color:#333}
.testimonials{top:790px;left:0;width:1200px;height:153px;background:var(--band)}
.testimonials h2{position:absolute;top:13px;left:318px;color:var(--white);font-size:16px;font-weight:700}
.quote{position:absolute;top:51px;width:182px;color:var(--white);font-size:7.6px;line-height:10.7px;padding-left:20px}
.quote::before{content:"\201C";position:absolute;left:0;top:-6px;font-size:24px;line-height:24px;color:var(--quote-mark);font-family:Georgia,serif}
.quote .name{margin-top:9px;font-weight:700;font-size:7.8px}
.clients{top:943px;left:0;width:1200px;height:67px;background:var(--strip)}
.client{position:absolute;top:23px;display:flex;align-items:center;gap:6px;color:var(--client);font-size:12.5px;font-weight:600;white-space:nowrap}
.client .dot{width:20px;height:20px;border-radius:50%;background:var(--client)}
.footer-nav{top:1021px;left:318px;font-size:8px;color:#777;display:flex;gap:13px}
.badge{top:1013px;height:27px;background:#e2e2e2}
.social{top:1018px;width:15px;height:15px;border-radius:3px;background:#6b8fc4}
</style>
</head>
<body>
<div class="abs account">Login Signup</div>
<div class="abs logo site-logo"><span class="dot"></span><span>Bright Path<br>Web Growth</span></div>
<nav class="abs nav"><span>Home</span><span>Services</span><span>About Us</span><span>Blog</span><span>Contact Us</span></nav>
<div class="abs rule" style="top:104px"></div>

<svg class="abs" style="top:105px;left:430px" width="560" height="322" aria-hidden="true">
  <line x1="30" y1="0" x2="165" y2="230" stroke="#eee" stroke-width="2"/>
  <line x1="535" y1="0" x2="455" y2="140" stroke="#eee" stroke-width="2"/>
</svg>
<h1 class="abs hero-title"><b>We Grow</b> your<br>Business <b>ONLINE</b></h1>
<div class="abs tagline">Clear Aim, Clear Plan, Clear Team,<br>Bright Path Web Growth</div>
<div class="abs hero-photo" role="img" aria-label="Smiling businessman in a dark suit holding an open laptop"></div>
<div class="abs rule" style="top:427px"></div>

<section class="abs service" style="top:458px;left:318px">
  <div class="head">
    <svg width="36" height="36" viewBox="0 0 36 36" aria-hidden="true"><rect x="2" y="4" width="32" height="20" fill="var(--brand)"/><rect x="14" y="1" width="8" height="3" fill="var(--brand)"/><circle cx="11" cy="14" r="5" fill="#fff"/><rect x="19" y="10" width="11" height="2" fill="#fff"/><rect x="19" y="15" width="11" height="2" fill="#fff"/><path d="M18 24 L12 34 M18 24 L24 34 M18 24 V34" stroke="var(--brand)" stroke-width="2"/></svg>
    <span>Consulting &amp;<br>Strategy Planning</span>
  </div>
  <p>Jujubes jelly beans pastry cake biscuit jujubes oat cake. Candy canes candy canes topping lemon drops liquorice. Faworki chocolate bar cookie tart powder tootsie roll macaroon liquorice.<br>Jujubes jelly beans pastry cake biscuit jujubes oat cake. Candy canes candy canes topping lemon drops liquorice. Faworki chocolate bar cookie tart powder tootsie roll macaroon liquorice.</p>
  <div class="more">MORE</div>
</section>
<section class="abs service" style="top:458px;left:606px">
  <div class="head">
    <svg width="40" height="36" viewBox="0 0 40 36" aria-hidden="true"><circle cx="15" cy="15" r="12" fill="none" stroke="var(--brand)" stroke-width="2"/><ellipse cx="15" cy="15" rx="5" ry="12" fill="none" stroke="var(--brand)" stroke-width="1.5"/><line x1="3" y1="15" x2="27" y2="15" stroke="var(--brand)" stroke-width="1.5"/><circle cx="26" cy="22" r="5" fill="#fff" stroke="var(--brand)" stroke-width="2"/><line x1="30" y1="26" x2="38" y2="32" stroke="var(--brand)" stroke-width="4"/></svg>
    <span>Search Engine Optimisation</span>
  </div>
  <p>Jujubes jelly beans pastry cake biscuit jujubes oat cake. Candy canes candy canes topping lemon drops liquorice. Faworki chocolate bar cookie tart powder tootsie roll macaroon liquorice.<br>Jujubes jelly beans pastry cake biscuit jujubes oat cake. Candy canes candy canes topping lemon drops liquorice. Faworki chocolate bar cookie tart powder tootsie roll macaroon liquorice.</p>
  <div class="more">MORE</div>
</section>
<section class="abs service" style="top:620px;left:318px">
  <div class="head">
    <svg width="36" height="36" viewBox="0 0 36 36" aria-hidden="true"><ellipse cx="18" cy="19" rx="15" ry="11" fill="var(--brand)"/><rect x="9" y="26" width="5" height="7" fill="var(--brand)"/><rect x="22" y="26" width="5" height="7" fill="var(--brand)"/><rect x="14" y="9" width="8" height="2" fill="#fff"/><circle cx="26" cy="16" r="1.5" fill="#fff"/></svg>
    <span style="margin-left:4px">Pay Per Click</span>
  </div>
  <p>Jujubes jelly beans pastry cake biscuit jujubes oat cake. Candy canes candy canes topping lemon drops liquorice. Faworki chocolate bar cookie tart powder tootsie roll macaroon liquorice.<br>Jujubes jelly beans pastry cake biscuit jujubes oat cake. Candy canes candy canes topping lemon drops liquorice. Faworki chocolate bar cookie tart powder tootsie roll macaroon liquorice.</p>
  <div class="more">MORE</div>
</section>
<section class="abs service" style="top:620px;left:606px">
  <div class="head">
    <svg width="36" height="36" viewBox="0 0 36 36" aria-hidden="true"><rect x="3" y="5" width="28" height="27" fill="var(--brand)"/><path d="M10 25 L17 12 M17 12 L24 22 M13 11 a8 8 0 0 1 12 4" stroke="#fff" stroke-width="1.8" fill="none"/><circle cx="10" cy="25" r="2" fill="#fff"/></svg>
    <span style="margin-left:4px">Re-Marketing</span>
  </div>
  <p>Jujubes jelly beans pastry cake biscuit jujubes oat cake. Candy canes candy canes topping lemon drops liquorice. Faworki chocolate bar cookie tart powder tootsie roll macaroon liquorice.<br>Jujubes jelly beans pastry cake biscuit jujubes oat cake. Candy canes candy canes topping lemon drops liquorice. Faworki chocolate bar cookie tart powder tootsie roll macaroon liquorice.</p>
  <div class="more">MORE</div>
</section>

<section class="abs testimonials">
  <h2>WHAT PEOPLE SAY:</h2>
  <div class="quote" style="left:318px">Jujubes jelly beans pastry cake biscuit jujubes oat cake. Candy canes candy canes topping lemon drops liquorice. Faworki chocolate bar cookie tart powder tootsie roll macaroon liquorice.<div class="name">NAME SURNAME</div>http://brightpathmarketing.com.au</div>
  <div class="quote" style="left:509px">Jujubes jelly beans pastry cake biscuit jujubes oat cake. Candy canes candy canes topping lemon drops liquorice. Faworki chocolate bar cookie tart powder tootsie roll macaroon liquorice.<div class="name">NAME SURNAME</div>http://brightpathmarketing.com.au</div>
  <div class="quote" style="left:705px">Jujubes jelly beans pastry cake biscuit jujubes oat cake. Candy canes candy canes topping lemon drops liquorice. Faworki chocolate bar cookie tart powder tootsie roll macaroon liquorice.<div class="name">NAME SURNAME</div>http://brightpathmarketing.com.au</div>
</section>

<section class="abs clients">
  <div class="client" style="left:319px"><span class="dot"></span>Bright Path</div>
  <div class="client" style="left:434px"><span class="dot"></span>Bright Path</div>
  <div class="client" style="left:548px"><span class="dot"></span>Bright Path</div>
  <div class="client" style="left:663px"><span class="dot"></span>Bright Path</div>
  <div class="client" style="left:787px"><span class="dot"></span>Bright Path</div>
</section>
<div class="abs rule" style="top:1010px"></div>

<nav class="abs footer-nav"><span>Home</span><span>About us</span><span>Services</span><span>Blog</span><span>Contact</span><span>Sitemap</span></nav>
<div class="abs badge" style="left:717px;width:30px"></div>
<div class="abs badge" style="left:762px;width:60px"></div>
<div class="abs social" style="left:849px"></div>
<div class="abs social" style="left:867px"></div>
</body>
</html>
```